Kivo Commercial Cleaning is lookong for a new business card design.

A fresh new design that's professional and stylish. We need a serious upgrade to our business cards. I have included pictures of our existing ones. Our clients include professional individuals and business owners. We woupdblike something professional and upbeat. Please have fun and see what you come uo with.

Target Market(s)

Property managers, business owners, facility managers and other similar professionals

Industry/Entity Type

Janitorial

Contact Information for Business Card

Name, cell, office number, email, web address

Font styles to use
Sans Serif

Colors

Designer to choose colors to be used in the design.

Requirements
Must have
• please use the green color in our logo
Nice to have
• Bar code
Should not have
• Address

```html
<!DOCTYPE html>
<html lang="en">
<head>
<meta charset="utf-8">
<title>Kivo Commercial Cleaning – Business Card</title>
<link href="https://fonts.googleapis.com/css2?family=Poppins:wght@400;500;600;700;800&display=swap" rel="stylesheet">
<style>
  :root {
    --green: #3dba53;
    --white: #ffffff;
    --backdrop: #d7d7d7;
    --shadow: rgba(0,0,0,0.18);
  }
  * { box-sizing: border-box; margin: 0; padding: 0; }
  html, body { width: 1200px; height: 846px; overflow: hidden; }
  body {
    background: var(--backdrop);
    font-family: "Poppins", sans-serif;
    position: relative;
  }
  .card {
    position: absolute;
    top: 263px;
    width: 560px;
    height: 320px;
    background: var(--white);
    box-shadow: 0 10px 28px var(--shadow);
    overflow: hidden;
  }
  .card--front { left: 30px; }
  .card--back { left: 610px; }

  /* brand name */
  .brand {
    font-family: "Poppins", sans-serif;
    font-weight: 700;
    letter-spacing: -1px;
    line-height: 1;
    display: flex;
    align-items: center;
    gap: 10px;
  }
  .brand__dot {
    width: 14px; height: 14px; border-radius: 50%;
  }

  /* front */
  .front__brand {
    position: absolute; left: 38px; top: 62px;
    color: var(--green); font-size: 70px;
  }
  .front__brand .brand__dot { background: var(--green); }
  .contacts {
    position: absolute; left: 282px; top: 44px;
    list-style: none;
  }
  .contacts__item {
    display: flex; align-items: center; gap: 9px;
    color: var(--green); font-size: 16px; font-weight: 400;
    height: 29px;
  }
  .contacts__icon {
    width: 22px; height: 22px; border-radius: 50%;
    background: var(--green);
    display: flex; align-items: center; justify-content: center;
    flex: none;
  }
  .stripe {
    position: absolute; left: 0; width: 100%; height: 3px;
    background: var(--green);
  }
  .stripe--one { top: 190px; }
  .stripe--two { top: 199px; }
  .front__band {
    position: absolute; left: 0; top: 208px; width: 100%; height: 112px;
    background: var(--green);
  }
  .front__name {
    position: absolute; right: 40px; top: 22px;
    color: var(--white); font-size: 27px; font-weight: 800;
  }

  /* back */
  .back__band {
    position: absolute; left: 0; top: 0; width: 100%; height: 172px;
    background: var(--green);
    display: flex; flex-direction: column; align-items: center; justify-content: center;
  }
  .back__brand { color: var(--white); font-size: 76px; }
  .back__brand .brand__dot { background: var(--white); }
  .back__tagline {
    color: var(--white); font-size: 15px; font-weight: 600; margin-top: 4px;
  }
  .services__title {
    position: absolute; left: 26px; right: 26px; top: 176px;
    display: flex; align-items: center; gap: 12px;
    color: var(--green); font-size: 20px; font-weight: 800; white-space: nowrap;
  }
  .services__title::before,
  .services__title::after {
    content: ""; flex: 1; height: 1px; background: var(--green);
  }
  .services {
    position: absolute; left: 18px; right: 18px; top: 216px;
    display: flex; justify-content: space-between; list-style: none;
  }
  .services__item {
    width: 80px; display: flex; flex-direction: column; align-items: center;
    color: var(--green); font-size: 10px; font-weight: 400;
    text-align: center; line-height: 1.2; text-transform: uppercase;
  }
  .services__icon {
    width: 40px; height: 40px; border-radius: 50%;
    background: var(--green); margin-bottom: 6px;
    display: flex; align-items: center; justify-content: center;
  }
</style>
</head>
<body>

<section class="card card--front" aria-label="Business card front">
  <div class="brand front__brand"><span>Kivo</span><span class="brand__dot"></span></div>

  <ul class="contacts">
    <li class="contacts__item">
      <span class="contacts__icon"><svg width="12" height="12" viewBox="0 0 24 24"><path d="M6 2l4 4-2 3a12 12 0 0 0 7 7l3-2 4 4-3 4C10 22 2 14 2 5z" fill="#fff"/></svg></span>
      (555) 310-2874
    </li>
    <li class="contacts__item">
      <span class="contacts__icon"><svg width="12" height="12" viewBox="0 0 24 24"><rect x="6" y="2" width="12" height="20" rx="2" fill="none" stroke="#fff" stroke-width="2.4"/><circle cx="12" cy="18" r="1.4" fill="#fff"/></svg></span>
      800-555-0182
    </li>
    <li class="contacts__item">
      <span class="contacts__icon"><svg width="12" height="12" viewBox="0 0 24 24"><rect x="2" y="5" width="20" height="14" fill="none" stroke="#fff" stroke-width="2.4"/><path d="M2 5l10 8 10-8" fill="none" stroke="#fff" stroke-width="2.4"/></svg></span>
      dana@kivocleaning.com
    </li>
    <li class="contacts__item">
      <span class="contacts__icon"><svg width="12" height="12" viewBox="0 0 24 24" fill="none" stroke="#fff" stroke-width="2"><circle cx="12" cy="12" r="10"/><ellipse cx="12" cy="12" rx="4" ry="10"/><path d="M2 12h20M4 7h16M4 17h16"/></svg></span>
      www.kivocleaning.com
    </li>
  </ul>

  <span class="stripe stripe--one"></span>
  <span class="stripe stripe--two"></span>
  <div class="front__band">
    <p class="front__name">Dana Whitfield</p>
  </div>
</section>

<section class="card card--back" aria-label="Business card back">
  <div class="back__band">
    <div class="brand back__brand"><span>Kivo</span><span class="brand__dot"></span></div>
    <p class="back__tagline">commercial cleaning</p>
  </div>

  <h2 class="services__title">WHO WE SERVICE</h2>
  <ul class="services">
    <li class="services__item">
      <span class="services__icon"><svg width="22" height="22" viewBox="0 0 24 24" fill="none" stroke="#fff" stroke-width="1.8"><path d="M12 21s-8-5-8-11a4 4 0 0 1 8-1 4 4 0 0 1 8 1c0 6-8 11-8 11z"/><path d="M5 12h4l2-3 2 5 2-2h4"/></svg></span>
      Medical
    </li>
    <li class="services__item">
      <span class="services__icon"><svg width="22" height="22" viewBox="0 0 24 24" fill="none" stroke="#fff" stroke-width="1.8"><rect x="5" y="3" width="14" height="18"/><path d="M8 7h2M14 7h2M8 11h2M14 11h2M8 15h2M14 15h2M11 21v-3h2v3"/></svg></span>
      Office<br>Buildings
    </li>
    <li class="services__item">
      <span class="services__icon"><svg width="22" height="22" viewBox="0 0 24 24" fill="none" stroke="#fff" stroke-width="1.8"><rect x="5" y="3" width="14" height="18" rx="1"/><path d="M8 13h2l1-3 2 5 1-2h2"/></svg></span>
      Health<br>Care
    </li>
    <li class="services__item">
      <span class="services__icon"><svg width="22" height="22" viewBox="0 0 24 24" fill="none" stroke="#fff" stroke-width="1.8"><path d="M8 16l8-8"/><circle cx="6" cy="18" r="3"/><circle cx="18" cy="6" r="3"/></svg></span>
      Industrial
    </li>
    <li class="services__item">
      <span class="services__icon"><svg width="22" height="22" viewBox="0 0 24 24" fill="none" stroke="#fff" stroke-width="1.8"><path d="M3 9l2-5h14l2 5z"/><path d="M4 9v11h16V9"/><rect x="7" y="13" width="4" height="7"/><rect x="13" y="13" width="4" height="3"/></svg></span>
      Retail
    </li>
    <li class="services__item">
      <span class="services__icon"><svg width="22" height="22" viewBox="0 0 24 24" fill="none" stroke="#fff" stroke-width="1.8"><path d="M12 6C9 4 5 4 3 5v14c2-1 6-1 9 1 3-2 7-2 9-1V5c-2-1-6-1-9 1z"/><path d="M12 6v14"/></svg></span>
      Places of<br>Worship
    </li>
  </ul>
</section>

</body>
</html>
```